Lanternby Consulting Business Card Design

Business Card Design for Lanternby Consulting. Lanternby Consulting is a boutique consultancy based in Atlanta, GA., that specializes in marketing strategy, organization planning, and leadership development. We provide solutions for small businesses and startups as well as Meridex 400 companies.

http://lanternbyconsulting.example/

Target Market(s)

We provide solutions for small businesses and startups as well as Meridex 400 companies.

Industry/Entity Type

Consulting

Contact Information for Business Card

Two sided business card with priority on contact information, logo, tag line (Inspiration to Dream More, Do More, Become More)

Colors

Designer to choose colors to be used in the design.

Requirements
Must have
• contact information, logo, tag line (Inspiration to Dream More, Do More, Become More)
• Simple no over communication.
Nice to have
• I would like to see different placements of logo and creative use of both sides of the card
Should not have
• Do not put too much information on the card.

```html
<!DOCTYPE html>
<html lang="en">
<head>
<meta charset="utf-8">
<title>Lanternby Consulting Business Card</title>
<link rel="stylesheet" href="https://fonts.googleapis.com/css2?family=Jost:wght@400;500;600&display=swap">
<style>
  :root {
    --backdrop: #5e5a55;
    --brand-blue: #3b72a0;
    --brand-blue-deep: #2d4f7c;
    --ink-dark: #0f1417;
    --ink-mid: #1f262a;
    --paper: #ffffff;
    --tag-ink: #1e140c;
    --icon-blue: #4a86bd;
  }
  * { margin: 0; padding: 0; box-sizing: border-box; }
  html, body { width: 1200px; height: 1200px; overflow: hidden; }
  body {
    background: var(--backdrop);
    font-family: "Jost", sans-serif;
    position: relative;
  }
  .card {
    position: absolute;
    width: 676px;
    height: 376px;
    overflow: hidden;
  }
  .card--front { left: 245px; top: 188px; background: var(--brand-blue); }
  .card--back { left: 249px; top: 688px; background: linear-gradient(180deg, var(--ink-dark), var(--ink-mid)); }

  .front__header { position: absolute; left: 0; top: 0; width: 676px; height: 133px; }
  .front__panel {
    position: absolute; left: 20px; top: 133px; width: 656px; height: 221px;
    background: linear-gradient(180deg, var(--ink-dark), var(--ink-mid));
  }
  .brand-name {
    position: absolute; color: var(--paper); font-weight: 500; white-space: nowrap;
  }
  .front__brand { left: 40px; top: 62px; font-size: 28px; }
  .tagline-stack {
    position: absolute; right: 27px; top: 50px; text-align: right;
    font-weight: 600; font-size: 20px; line-height: 22.5px; color: var(--tag-ink);
  }
  .contact {
    position: absolute; left: 20px; font-size: 22px; line-height: 28px; color: var(--paper);
    display: flex; align-items: center; gap: 12px; white-space: nowrap;
  }
  .contact svg { width: 16px; height: 16px; fill: var(--icon-blue); }
  .contact--phone { top: 139px; }
  .contact--email { top: 169px; }
  .location {
    position: absolute; right: 27px; top: 171px; font-size: 19px; line-height: 24px; color: var(--paper);
  }

  .back__brand { left: 0; width: 676px; top: 192px; text-align: center; font-size: 40px; }
  .back__tagline {
    position: absolute; left: 0; width: 676px; top: 301px; text-align: center;
    font-size: 20px; color: var(--paper); white-space: nowrap;
  }
  .back__strip { position: absolute; left: 0; bottom: 0; width: 676px; height: 22px; background: var(--brand-blue); }
</style>
</head>
<body>
  <section class="card card--front" aria-label="Card front">
    <svg class="front__header" viewBox="0 0 676 133" aria-hidden="true">
      <defs>
        <linearGradient id="headerBlue" x1="0" y1="0" x2="1" y2="0.4">
          <stop offset="0" stop-color="#3b72a0"/>
          <stop offset="0.62" stop-color="#3b72a0"/>
          <stop offset="0.85" stop-color="#2d4f7c"/>
        </linearGradient>
      </defs>
      <rect width="676" height="133" fill="url(#headerBlue)"/>
      <polygon points="296,0 676,0 676,133 395,133" fill="#ffffff"/>
    </svg>
    <div class="brand-name front__brand">Lanternby Consulting</div>
    <div class="tagline-stack">
      <div>Inspiration to Dream More</div>
      <div>Do More</div>
      <div>Become More</div>
    </div>
    <div class="front__panel">
      <div class="contact contact--phone">
        <svg viewBox="0 0 24 24" aria-hidden="true"><path d="M6.6 2.5l3 3.2-1.8 2.4c1.2 2.8 3.3 5 6.1 6.3l2.4-1.8 3.2 3-1.6 3.4c-7.8-.4-14-6.6-14.4-14.4z"/></svg>
        <span>404-555-0187</span>
      </div>
      <div class="contact contact--email">
        <svg viewBox="0 0 24 24" aria-hidden="true"><path d="M2 5h20v2.2l-10 6-10-6zM2 9.5l10 6 10-6V19H2z"/></svg>
        <span>jordan@lanternbyconsulting.example</span>
      </div>
      <div class="location">Atlanta, GA.</div>
    </div>
  </section>

  <section class="card card--back" aria-label="Card back">
    <div class="brand-name back__brand">Lanternby Consulting</div>
    <p class="back__tagline">Inspiration to Drem More, Do More, Become More</p>
    <div class="back__strip"></div>
  </section>
</body>
</html>
```